COMPANY NAME: Brightmoor Paths: Task Description: We are a new UK based business with global rea

Target Market

- Personal and professional development – 30-55 age group, corporate leaders, Eastern European and Asian markets
- On-assignment projects – Corporate market – Eastern European and Asian Markets
- Property investment - 35-65 age group, Europe, USA, Australia

What we need

We need logos and brand design for a suite of web platforms (website, twitter and Facebook profile). We would like to have a cohesive and consistent look across all of our online platforms. The design suite must therefore include social media logos, backgrounds and headers. Specifically we are looking for:

a. Facebook header/page design: likely to have a more youthful look

b. Website: Header, background and layout that is responsive to devices, iPhone primarily, then tablet, then PC (we have purchased a website building package from GoDaddy so if you are familiar with one of their themes, it would be great to have a design that fits with a theme you would recommend); Design should be able to accommodate a place to position video in the medium term but an image in the short term.

c. LinkedIn: header/logo; more corporate look

d. Twitter: background/logo

e. Powerpoint template: background and logo - simple and soft background not busy

f. Electronic Newsletter: logo, header and sidebar; simple and soft background not busy

h. Business card: sophisticated and simple

Colors

We have in mind a preference for colors from the purple family, maybe lavender, so as to appeal to all genders and age groups. Though we are happy to go with a recommendation if you think otherwise.

We would like a look that is professional, airy, bright, fresh, futuristic, insightful, friendly.

Ethos of the brand

- experiencing opportunity and being fulfilled in a changing world
- services are facilitated through insights
- support provided through our product, services and tailored approach to coaching/partnerships (which includes private client match-making)
- we are service providers and passionate about quality and modern leadership skills at all stages in life.

The company name is "Brightmoor Paths” - our main message is helping people move to the next level - through investments, personal and professional growth.

Some of our messaging

1. International Leadership in a new world.

2. New technology;

3. Informed;

4. Positively Influential

5. Making a difference;

6. Empowered;

7. Risk free investments;

8. Commercial opportunity;

9. Fulfilled living;

10. Carefree and Fun Living;

11. Progression;

12. Open-minded

13. Energy/dynamic

The Business:
The business is to move people very quickly out of situations that hold them back. the situations could be their own personal situations; their career; their jobs; their teams; their ideas; their finances; their financial opportunities. Remove their fears and give them the strategies to take action. The team are international and have 40 years experience between them in this area.

We do want to come across modern and dynamic, customer outcome focussed, building long-term relationships; international.
Updates

Project Deadline Extended
Reason: We have not found the right designs - we are not just looking for a website design but also images and logos. Most images we can see in the designs are stock images - very standard. We need an image which will be the face of the company, like the shop front window. This main image will be used on social media (top image) and also the home page of the website.

Target Market(s)

30-55 years
Eastern Europe; UK; Asia; Africa; Middle East
Personal, Professional, Corporate, and Financial Growth

Industry/Entity Type

Business Service

Contact Information for Business Card

Simple and stylish
the 3 areas of the business on the reverse -

International look - Offices in UK and San Francisco

Company name
web address www.brightmoorpath.com
email director@brightmoorpath.com
Facebook brightmoor path
LinkedIn Brightmoor Path
Twitter Brightmoor Path
Telephone: +44 (0) 712 348 9561

Logo Text

Something that symbolises unlimited growth - probably not text - could use the word INSIGHT in some way

Number of Pages Required

1 page

Colors
e4daeb
f3f1f8
ffffff

Requirements
Must have
• social media symbols and address
• company name
• Harriet Lomax
• Director
• Telephone +44 (0) 712 348 9561
• Website name www.brightmoorpath.co.uk
• Reverse of Card:
• Discreet, Fast, Brightmoor Consultancy
• Corporate, Professional, Personal & Property Investment
Nice to have
• not too angular; soft lines; not too cluttered (possibly social media on the reverse and just logo, name, number on the front?
Should not have
• too busy

```html
<!DOCTYPE html>
<html lang="en">
<head>
<meta charset="utf-8">
<title>Brightmoor Path</title>
<link href="https://fonts.googleapis.com/css2?family=Oswald:wght@400;500&family=Roboto:wght@400;500;700&display=swap" rel="stylesheet">
<style>
:root{
  --ink:#2b2a2f;
  --ink-soft:#3b3a40;
  --text:#55545a;
  --muted:#7b7a80;
  --lavender:#e4daeb;
  --lavender-pale:#f3f1f8;
  --lavender-deep:#b9a6c9;
  --purple:#8b7a9e;
  --white:#ffffff;
  --footer:#2e2d33;
}
*{box-sizing:border-box;margin:0;padding:0}
html,body{width:1200px;height:2836px;overflow:hidden}
body{font-family:"Roboto",Arial,sans-serif;color:var(--text);background:var(--white);position:relative}
section,header,footer{position:absolute;left:0;width:1200px}

/* hero + menu */
.hero{top:0;height:592px;background:linear-gradient(160deg,#3a3840 0%,#1d1c21 60%,#141317 100%);overflow:hidden}
.hero-photo{position:absolute;inset:0;background:radial-gradient(ellipse at 55% 60%,rgba(120,110,130,.35),rgba(20,19,23,0) 65%)}
.brand{position:absolute;left:48px;top:30px;font-family:"Oswald",sans-serif;font-weight:500;font-size:30px;color:var(--white);letter-spacing:.3px}
.close-btn{position:absolute;right:52px;top:22px;width:52px;height:52px;border:2px solid var(--white);display:flex;align-items:center;justify-content:center}
.main-menu{position:absolute;top:122px;left:0;width:1200px;list-style:none;text-align:center}
.main-menu li{font-family:"Oswald",sans-serif;font-size:30px;letter-spacing:8px;color:var(--white);line-height:58px}
.main-menu li span{border-bottom:2px solid rgba(255,255,255,.85);padding-bottom:2px}
.hero-social{position:absolute;top:498px;left:0;width:1200px;display:flex;justify-content:center;gap:26px}
.hero-social i{width:20px;height:20px;border-radius:50%;background:var(--white);display:block}
.slider-dots{position:absolute;right:30px;top:310px;display:flex;flex-direction:column;gap:12px}
.slider-dots i{width:10px;height:10px;border-radius:50%;background:rgba(255,255,255,.35);display:block}
.slider-dots i:first-child{background:var(--white)}

/* section headings */
.sec-title{display:flex;align-items:center;font-family:"Oswald",sans-serif;font-size:34px;color:var(--ink);height:48px}
.sec-title .word{padding-right:8px;border-bottom:4px solid var(--ink);line-height:40px}
.sec-title .tag{background:var(--ink-soft);color:var(--white);padding:0 38px 0 16px;line-height:48px;clip-path:polygon(0 0,88% 0,100% 50%,88% 100%,0 100%)}
.on-dark .word{color:var(--white);border-color:var(--white)}
.on-dark .tag{background:var(--lavender);color:var(--ink)}
.btn{display:inline-block;background:var(--ink-soft);color:var(--white);font-size:16px;font-weight:500;padding:0 22px;line-height:40px;border-radius:3px}

/* about */
.about{top:592px;height:400px;background:var(--white)}
.about .sec-title{position:absolute;left:88px;top:52px}
.about-copy{position:absolute;left:100px;top:128px;width:570px;font-size:15px;line-height:24px}
.about-copy .lead{font-weight:700;color:var(--ink);font-size:17px;margin-bottom:14px}
.about-copy p{margin-bottom:12px}
.about .btn{position:absolute;left:100px;top:304px}
.video-frame{position:absolute;left:712px;top:60px;width:388px;height:282px;box-shadow:0 8px 22px rgba(0,0,0,.25);background:linear-gradient(135deg,#6d6672,#3c3843 55%,#8a8290)}
.video-play{position:absolute;left:168px;top:110px;width:56px;height:40px;border-radius:8px;background:#c0392b;display:flex;align-items:center;justify-content:center}
.video-bar{position:absolute;left:0;bottom:0;width:100%;height:28px;background:rgba(0,0,0,.55)}

/* consultancy */
.consultancy{top:992px;height:496px;background:var(--lavender)}
.consultancy .sec-title{position:absolute;left:460px;top:78px}
.services{position:absolute;top:160px;left:0;width:1200px;display:flex;justify-content:center;gap:0}
.service{width:300px;text-align:center}
.pin{width:170px;height:190px;margin:0 auto}
.service h3{font-family:"Roboto",sans-serif;font-weight:500;font-size:22px;color:var(--ink);margin-top:4px}
.service p{font-size:14px;line-height:21px;color:var(--muted);width:220px;margin:8px auto 0}

/* assignment */
.assignment{top:1488px;height:572px;background:linear-gradient(180deg,#2a292e,#1e1d22)}
.assignment .sec-title{position:absolute;left:470px;top:52px}
.cards{position:absolute;top:144px;left:108px;display:flex;gap:36px}
.card{width:304px;height:392px;background:var(--white);padding:16px;position:relative}
.card-photo{height:184px;background:linear-gradient(135deg,#8f8995,#4d4953 60%,#a59fab)}
.card h3{font-size:18px;font-weight:700;color:var(--ink);margin-top:20px}
.card p{font-size:13px;line-height:20px;color:var(--muted);margin-top:8px}
.card .btn{position:absolute;left:16px;bottom:16px;font-size:15px;line-height:36px;padding:0 18px}

/* private client */
.client{top:2060px;height:468px;background:var(--white)}
.client .sec-title{position:absolute;left:96px;top:52px}
.ticks{position:absolute;left:100px;top:128px;list-style:none}
.ticks li{display:flex;align-items:center;gap:14px;font-size:17px;font-weight:500;color:var(--ink);line-height:42px}
.client .btn{position:absolute;left:100px;top:398px}
.devices{position:absolute;left:690px;top:40px;width:470px;height:420px;background:radial-gradient(ellipse at 60% 55%,#e9e3ee 0%,#f6f4f8 55%,#ffffff 80%)}

/* footer */
.site-footer{top:2528px;height:244px;background:var(--footer);color:#cfcdd4}
.foot-brand{position:absolute;left:96px;top:54px;font-family:"Oswald",sans-serif;font-size:32px;font-weight:500;color:var(--white)}
.foot-social{position:absolute;left:110px;top:112px;display:flex;gap:14px}
.foot-social i{width:30px;height:30px;border-radius:50%;background:#4a4950;display:block}
.foot-col{position:absolute;top:32px}
.foot-col h4{font-family:"Roboto",sans-serif;font-weight:500;font-size:20px;color:var(--white);margin-bottom:18px}
.links{left:400px;list-style:none}
.links li{font-size:13px;line-height:23px;display:flex;align-items:center;gap:8px}
.links li::before{content:"";width:6px;height:6px;border-radius:50%;background:var(--lavender-deep)}
.contact{left:572px;font-size:12px;line-height:17px}
.contact b{display:block;color:var(--white);font-weight:500}
.contact div{margin-bottom:10px}
.subscribe{left:864px;width:250px;font-size:13px;line-height:19px}
.sub-form{display:flex;margin-top:18px}
.sub-form span{flex:1;background:#3f3e45;line-height:40px;padding-left:12px;color:#9c9aa2}
.sub-form b{width:40px;background:var(--lavender);color:var(--ink);text-align:center;line-height:40px;font-weight:500}
.copyright{position:absolute;left:0;top:2772px;width:1200px;height:64px;background:var(--lavender);display:flex;align-items:center;justify-content:center;font-size:13px;color:var(--ink-soft)}
</style>
</head>
<body>

<header class="hero">
  <div class="hero-photo" role="img" aria-label="Dimmed photograph of a business meeting behind the menu"></div>
  <div class="brand">Brightmoor Path</div>
  <div class="close-btn"><svg width="18" height="18" viewBox="0 0 18 18"><path d="M2 2L16 16M16 2L2 16" stroke="#fff" stroke-width="2.6"/></svg></div>
  <ul class="main-menu">
    <li><span>ABOUT YOU</span></li>
    <li><span>ABOUT US</span></li>
    <li><span>OUR VALUES</span></li>
    <li><span>TESTIMONIALS</span></li>
    <li><span>SOCIAL MEDIA</span></li>
    <li><span>NEWS ALERT</span></li>
  </ul>
  <div class="hero-social"><i></i><i></i><i></i></div>
  <div class="slider-dots"><i></i><i></i><i></i><i></i></div>
</header>

<section class="about">
  <h2 class="sec-title"><span class="word">About</span><span class="tag">Brightmoor Path</span></h2>
  <div class="about-copy">
    <p class="lead">Hello and welcome to the company that works with you on your terms</p>
    <p>If you seek an experienced and trusted partner to work with you on an assignment or simply want some strategies to move your personal or professional life forward, you are in the right place.</p>
    <p>If you feel that the pace of change in business is so fast that leading well seems out of reach, we help you get up to speed quickly and with confidence.</p>
  </div>
  <span class="btn">Read More</span>
  <div class="video-frame" role="img" aria-label="Video still of a team seated around a meeting table">
    <div class="video-play"><svg width="18" height="18" viewBox="0 0 18 18"><path d="M4 2L16 9L4 16Z" fill="#fff"/></svg></div>
    <div class="video-bar"></div>
  </div>
</section>

<section class="consultancy">
  <h2 class="sec-title"><span class="word">Our</span><span class="tag">Consultancy</span></h2>
  <div class="services">
    <div class="service">
      <svg class="pin" viewBox="0 0 170 190"><path d="M85 186L62 150A80 80 0 1 1 108 150Z" fill="#b9a6c9"/><circle cx="85" cy="80" r="66" fill="#8b7a9e"/><circle cx="85" cy="80" r="58" fill="none" stroke="#fff" stroke-width="2"/><g fill="#fff"><circle cx="85" cy="64" r="9"/><path d="M69 96a16 14 0 0 1 32 0Z"/><circle cx="62" cy="70" r="7"/><path d="M50 96a12 12 0 0 1 22-6v6Z"/><circle cx="108" cy="70" r="7"/><path d="M98 90a12 12 0 0 1 22 6h-22Z"/></g></svg>
      <h3>Professional and Personal</h3>
      <p>Practical coaching that helps you rethink goals, grow with purpose and lead with confidence.</p>
    </div>
    <div class="service">
      <svg class="pin" viewBox="0 0 170 190"><path d="M85 186L62 150A80 80 0 1 1 108 150Z" fill="#b9a6c9"/><circle cx="85" cy="80" r="66" fill="#8b7a9e"/><circle cx="85" cy="80" r="58" fill="none" stroke="#fff" stroke-width="2"/><g fill="#fff"><rect x="58" y="56" width="42" height="30" rx="4"/><path d="M64 86l-6 10 14-10Z"/><circle cx="106" cy="84" r="9"/><path d="M92 108a14 12 0 0 1 28 0Z"/></g><g stroke="#8b7a9e" stroke-width="3"><path d="M65 66h28M65 75h20"/></g></svg>
      <h3>Next Generation Leaders</h3>
      <p>Building tomorrow's leaders through mentoring, insight and tailored programmes for growing teams.</p>
    </div>
    <div class="service">
      <svg class="pin" viewBox="0 0 170 190"><path d="M85 186L62 150A80 80 0 1 1 108 150Z" fill="#b9a6c9"/><circle cx="85" cy="80" r="66" fill="#8b7a9e"/><circle cx="85" cy="80" r="58" fill="none" stroke="#fff" stroke-width="2"/><rect x="56" y="54" width="58" height="40" rx="3" fill="none" stroke="#fff" stroke-width="4"/><path d="M64 86l12-12 10 8 18-18" fill="none" stroke="#fff" stroke-width="4"/><path d="M76 94l-6 14M94 94l6 14" stroke="#fff" stroke-width="4"/></svg>
      <h3>Consultation Options</h3>
      <p>Flexible sessions to explore your options and shape a clear plan for the next step.</p>
    </div>
  </div>
</section>

<section class="assignment" role="region" aria-label="Assignment services over a dimmed photograph of an office">
  <h2 class="sec-title on-dark"><span class="word">On</span><span class="tag">Assignment</span></h2>
  <div class="cards">
    <article class="card">
      <div class="card-photo" role="img" aria-label="Photograph of colleagues working together at a laptop"></div>
      <h3>Team Cohesion Strategy</h3>
      <p>We bring scattered teams together around shared goals, clear roles and trust, so every member pulls in the same direction.</p>
      <span class="btn">Read More</span>
    </article>
    <article class="card">
      <div class="card-photo" role="img" aria-label="Photograph of a busy open-plan office"></div>
      <h3>Go To Market Strategy</h3>
      <p>We shape launch plans that test demand early, reach the right buyers and turn ideas into steady revenue fast.</p>
      <span class="btn">Read More</span>
    </article>
    <article class="card">
      <div class="card-photo" role="img" aria-label="Photograph of a business meeting around a table"></div>
      <h3>Internationalisation Strategy</h3>
      <p>We guide firms entering new regions with local insight, partner introductions and a clear roadmap for growth abroad.</p>
      <span class="btn">Read More</span>
    </article>
  </div>
</section>

<section class="client">
  <h2 class="sec-title"><span class="word">Property</span><span class="tag">Private Client</span></h2>
  <ul class="ticks">
    <li><svg width="22" height="22" viewBox="0 0 22 22"><rect x="1" y="1" width="20" height="20" rx="3" fill="none" stroke="#2b2a2f" stroke-width="2"/><path d="M5 11l4 4 8-9" fill="none" stroke="#2b2a2f" stroke-width="2.6"/></svg>Promotion and cash buyer matching.</li>
    <li><svg width="22" height="22" viewBox="0 0 22 22"><rect x="1" y="1" width="20" height="20" rx="3" fill="none" stroke="#2b2a2f" stroke-width="2"/><path d="M5 11l4 4 8-9" fill="none" stroke="#2b2a2f" stroke-width="2.6"/></svg>Investment: high return projects.</li>
    <li><svg width="22" height="22" viewBox="0 0 22 22"><rect x="1" y="1" width="20" height="20" rx="3" fill="none" stroke="#2b2a2f" stroke-width="2"/><path d="M5 11l4 4 8-9" fill="none" stroke="#2b2a2f" stroke-width="2.6"/></svg>Commercial: Hotels and Senior Housing.</li>
    <li><svg width="22" height="22" viewBox="0 0 22 22"><rect x="1" y="1" width="20" height="20" rx="3" fill="none" stroke="#2b2a2f" stroke-width="2"/><path d="M5 11l4 4 8-9" fill="none" stroke="#2b2a2f" stroke-width="2.6"/></svg>Prestige Residential: US, Australia, UK.</li>
  </ul>
  <span class="btn">Read More</span>
  <div class="devices" role="img" aria-label="Illustration of the website shown on a phone, tablet and desktop screen"></div>
</section>

<footer class="site-footer">
  <div class="foot-brand">Brightmoor Path</div>
  <div class="foot-social"><i></i><i></i><i></i><i></i><i></i></div>
  <ul class="foot-col links">
    <h4>Quick Links</h4>
    <li>About You</li><li>About Us</li><li>Our Values</li><li>Testimonials</li><li>Social Media</li><li>News Alert</li>
  </ul>
  <div class="foot-col contact">
    <h4>Contact Us</h4>
    <div><b>BRIGHTMOOR PATH</b>Registered number<br>09876543</div>
    <div><b>PHONE</b>+44 (0) 712 348 9561</div>
    <div><b>Mail</b>director@brightmoorpath.com</div>
  </div>
  <div class="foot-col subscribe">
    <h4>Subscribe</h4>
    <p>Sign up for news, insights and updates delivered straight to your inbox.</p>
    <div class="sub-form"><span>Email</span><b>Go</b></div>
  </div>
</footer>
<div class="copyright">Copyright © Brightmoor Path. All Right Reserved.</div>

</body>
</html>
```